Professional Services (B-2-B) Business Cards (Front & Back)

Quintarion is a business-to-business professional services company in the legal sector. They typically present to c-suite and executive functions who are looking for providers with expertise, and experience. Our business card should look and feel professional and contemporary, but we are not a startup tech company, so we want the tone to be more mature.

```html
<!DOCTYPE html>
<html lang="en">
<head>
<meta charset="UTF-8">
<title>Quintarion Business Cards</title>
<link rel="stylesheet" href="https://fonts.googleapis.com/css2?family=Oswald:wght@500&family=Lato:wght@300;400&display=swap">
<style>
  :root {
    --backdrop: #3b3c3e;
    --card-blue: #0d3f9e;
    --card-blue-deep: #0a3282;
    --silver: #d3d7de;
    --silver-soft: #aeb4be;
  }
  * { margin: 0; padding: 0; box-sizing: border-box; }
  html, body { width: 1200px; height: 900px; overflow: hidden; }
  body {
    background: var(--backdrop);
    display: flex;
    flex-direction: column;
    align-items: center;
    justify-content: center;
    gap: 60px;
    font-family: "Lato", sans-serif;
  }
  .card {
    width: 560px;
    height: 320px;
    background: radial-gradient(ellipse at 40% 40%, var(--card-blue) 0%, var(--card-blue-deep) 100%);
    border-radius: 3px;
    position: relative;
    overflow: hidden;
  }
  .card--front {
    display: flex;
    align-items: center;
    justify-content: center;
  }
  .brand {
    display: flex;
    align-items: center;
    gap: 18px;
  }
  .brand__dot {
    width: 18px;
    height: 18px;
    border-radius: 50%;
    background: var(--silver);
  }
  .brand__name {
    font-family: "Lato", sans-serif;
    font-weight: 400;
    font-size: 30px;
    letter-spacing: 0.42em;
    color: var(--silver);
  }
  .card--back {
    display: flex;
    align-items: center;
    padding: 0 48px 0 44px;
  }
  .identity {
    text-align: right;
    padding-right: 18px;
    margin-top: -40px;
    white-space: nowrap;
  }
  .identity__name {
    font-family: "Oswald", sans-serif;
    font-weight: 500;
    font-size: 26px;
    letter-spacing: 0.02em;
    color: var(--silver);
    line-height: 1.1;
    text-transform: uppercase;
  }
  .identity__title {
    font-weight: 300;
    font-size: 14px;
    letter-spacing: 0.03em;
    color: var(--silver-soft);
    text-transform: uppercase;
    margin-top: 2px;
  }
  .divider {
    width: 1px;
    height: 120px;
    background: var(--silver-soft);
    flex: none;
  }
  .contact {
    list-style: none;
    padding-left: 18px;
    margin-top: 40px;
    white-space: nowrap;
  }
  .contact__item {
    display: flex;
    align-items: center;
    gap: 7px;
    font-size: 15px;
    color: var(--silver);
    line-height: 1.45;
    letter-spacing: 0.01em;
  }
  .contact__icon { width: 12px; height: 12px; flex: none; }
</style>
</head>
<body>
  <section class="card card--front">
    <div class="brand">
      <span class="brand__dot"></span>
      <span class="brand__name">QUINTARION</span>
    </div>
  </section>

  <section class="card card--back">
    <div class="identity">
      <p class="identity__name">Mark Holloway</p>
      <p class="identity__title">President &amp; CEO</p>
    </div>
    <div class="divider"></div>
    <ul class="contact">
      <li class="contact__item">
        <svg class="contact__icon" viewBox="0 0 16 16" fill="#d3d7de"><path d="M3 1l3 3-1.5 2a9 9 0 0 0 5.5 5.5L12 10l3 3-2 2C7 15 1 9 1 3z"/></svg>
        (415) 555 - 0142
      </li>
      <li class="contact__item">
        <svg class="contact__icon" viewBox="0 0 16 16" fill="none" stroke="#d3d7de" stroke-width="1.6"><rect x="4" y="1" width="8" height="14" rx="1.5"/><line x1="7" y1="12.5" x2="9" y2="12.5"/></svg>
        (203) 555 - 0187
      </li>
      <li class="contact__item">
        <svg class="contact__icon" viewBox="0 0 16 16" fill="none" stroke="#d3d7de" stroke-width="1.6"><rect x="1" y="3" width="14" height="10" rx="1"/><path d="M1 4l7 5 7-5"/></svg>
        mholloway@quintarion.tech
      </li>
      <li class="contact__item">
        <svg class="contact__icon" viewBox="0 0 16 16" fill="none" stroke="#d3d7de" stroke-width="1.4"><circle cx="8" cy="8" r="6.5"/><ellipse cx="8" cy="8" rx="3" ry="6.5"/><line x1="1.5" y1="8" x2="14.5" y2="8"/></svg>
        www.quintarion.tech
      </li>
    </ul>
  </section>
</body>
</html>
```